Morning Lantern Drive Flyer

I need a DL sized flyer that will be sent out to participants in our Morning Lantern Drive - sharing 1million Lantern Cards with the world. This flyer will form the first tangible item most of our community will receive from Brightwater Circle, so it needs to be able to communicate our goal of inspiring change, possibility, kindness and love in the world.

Target Market(s)

Women aged 30 - 50, sophisticated, generous, philanthropy minded, contemporary, elegant

Font styles to use
Sans Serif
Other font styles liked:
• Raleway

Colors

Designer to choose colors to be used in the design.

Requirements
Must have
• Must be DL size - i.e. one third of an A4. On one side the flyer must also include space for the Lantern Cards to be stuck - the lantern cards are Stickmarks that are 3in (76mm) square.
• The logo must be included somewhere, along with the website and social media icons - brightwatercircle.com.au, Facebook, Instagram, Twitter all @brightwatercircle.
• The copy for the flyer is:
• Thank you so much for helping us to reach our goal of having one million lantern cards out in the world. Share one of our notes with a friend, a family member, with a total stranger, or perhaps just with yourself. And remember that you might just be Brightwater Circle in someone else's day.
• Share the story of your lantern cards on social media with the hashtag #morninglanterndrive or send us a photo and your story to lantern@brightwatercircle.com.au

```html
<!DOCTYPE html>
<html lang="en">
<head>
<meta charset="utf-8">
<title>Morning Lantern Drive – DL Flyer</title>
<link href="https://fonts.googleapis.com/css2?family=Bebas+Neue&family=Varela+Round&family=Raleway:wght@500;600&display=swap" rel="stylesheet">
<style>
  :root{
    --stage-light:#e6e6e6;
    --stage-dark:#9a9a9a;
    --paper:#f1f1f1;
    --panel:#ececec;
    --ink:#3a3a3a;
    --white:#ffffff;
    --note-grey:#a9a9a9;
    --orange:#f39a1e;
    --yellow:#f8c21b;
    --magenta:#e0407a;
    --purple:#5b2b84;
    --teal:#1f6f63;
    --paint:linear-gradient(170deg,var(--orange) 0%,var(--yellow) 38%,#e8a020 55%,var(--purple) 85%,#3e1f66 100%);
    --band:linear-gradient(100deg,var(--orange) 0%,var(--yellow) 35%,#e86a4a 65%,var(--purple) 100%);
  }
  *{box-sizing:border-box;margin:0;padding:0}
  html,body{width:1200px;height:1000px;overflow:hidden}
  body{background:radial-gradient(ellipse at 50% 50%,var(--stage-light) 0%,#c4c4c4 60%,var(--stage-dark) 100%);position:relative;font-family:'Varela Round',sans-serif}
  .side{position:absolute;top:27px;height:939px;box-shadow:0 0 10px rgba(0,0,0,.35);overflow:hidden}
  /* front */
  .front{left:198px;width:408px;background:var(--paper)}
  .front-paint{position:absolute;left:194px;top:0;width:214px;height:100%;background:var(--paint)}
  .logo-disc{position:absolute;left:45px;top:118px;width:300px;height:300px;border-radius:50%;background:var(--paper);display:flex;align-items:center;justify-content:center}
  .logo-ring{width:262px;height:262px;border-radius:50%;border:7px solid var(--magenta);border-top-color:var(--orange);border-right-color:var(--yellow);border-bottom-color:var(--purple);display:flex;align-items:center;justify-content:center}
  .logo-name{font-family:'Raleway',sans-serif;font-weight:600;font-size:26px;color:var(--teal);text-align:center;line-height:1.15}
  .frame-lines{position:absolute;left:0;top:0}
  .headline-left{position:absolute;left:30px;top:426px;width:148px;text-align:right;font-family:'Bebas Neue',sans-serif;font-size:30px;line-height:1;color:#c9772e}
  .headline-right{position:absolute;left:212px;top:430px;font-family:'Bebas Neue',sans-serif;font-size:40px;color:var(--white);text-shadow:1px 1px 3px rgba(0,0,0,.6)}
  .copy{position:absolute;left:32px;top:543px;width:350px;font-family:'Bebas Neue',sans-serif;font-size:20px;line-height:1.25;color:var(--white);text-shadow:1px 1px 3px rgba(0,0,0,.75)}
  .copy ul{list-style:none;margin:14px 0 18px}
  .copy li{position:relative;padding-left:22px}
  .copy li::before{content:"";position:absolute;left:2px;top:5px;width:12px;height:12px;border-radius:50%;background:var(--teal)}
  .handle{position:absolute;left:0;width:100%;top:852px;text-align:center;font-family:'Bebas Neue',sans-serif;font-size:15px;color:var(--white);text-shadow:1px 1px 2px rgba(0,0,0,.7)}
  .social{position:absolute;top:864px;width:40px;height:40px;border-radius:50%;border:3px solid var(--orange);background:rgba(255,255,255,.25)}
  .social.one{left:34px}.social.two{left:173px}.social.three{left:324px;border-color:var(--white)}
  .website{position:absolute;left:0;width:100%;top:920px;text-align:center;font-family:'Bebas Neue',sans-serif;font-size:14px;color:var(--white);text-shadow:1px 1px 2px rgba(0,0,0,.7)}
  /* back */
  .back{left:651px;width:397px;background:var(--paper)}
  .band{position:absolute;left:0;width:100%;background:var(--band);display:flex;align-items:center;justify-content:center;color:var(--white);text-shadow:1px 1px 3px rgba(0,0,0,.5)}
  .band.title{top:0;height:180px;flex-direction:column;font-family:'Raleway',sans-serif;font-weight:500;font-size:40px;line-height:1.1}
  .band.tag{top:378px;height:65px;font-size:25px}
  .band.mail{top:549px;height:66px;font-size:18px}
  .panel{position:absolute;left:0;width:100%;background:var(--panel);display:flex;align-items:center;justify-content:center;text-align:center;font-size:25px;line-height:1.35;color:var(--ink);text-shadow:1px 1px 3px rgba(0,0,0,.35)}
  .panel.story{top:180px;height:198px}
  .panel.send{top:443px;height:106px}
  .card-heading{position:absolute;right:24px;top:624px;text-align:right;font-family:'Bebas Neue',sans-serif;font-size:40px;line-height:.95;color:var(--white);text-shadow:1px 1px 3px rgba(0,0,0,.6)}
  .card-space{position:absolute;left:27px;top:673px}
</style>
</head>
<body>

<section class="side front">
  <div class="front-paint" role="img" aria-label="Abstract painted texture in orange, yellow and purple"></div>

  <div class="logo-disc">
    <div class="logo-ring">
      <p class="logo-name">Brightwater<br>Circle</p>
    </div>
  </div>

  <svg class="frame-lines" width="408" height="939" viewBox="0 0 408 939" aria-hidden="true">
    <polyline points="30,470 200,470 200,384 360,384" fill="none" stroke="#fff" stroke-width="3"/>
    <polyline points="8,851 112,851 112,907 268,907 268,851 400,851" fill="none" stroke="#fff" stroke-width="3"/>
  </svg>

  <p class="headline-left">Brightwater</p>
  <p class="headline-right">Circle</p>

  <div class="copy">
    <p>Thank you so much for helping us to reach our goal of having one million lantern cards out in the world.</p>
    <ul>
      <li>Share one of our notes with a friend,</li>
      <li>a family member,</li>
      <li>with a total stranger,</li>
      <li>or perhaps just with yourself.</li>
    </ul>
    <p>And remember that you might just be Brightwater Circle in someone else's day.</p>
  </div>

  <p class="handle">@brightwatercircle</p>
  <span class="social one"></span>
  <span class="social two"></span>
  <span class="social three"></span>
  <p class="website">www.brightwatercircle.com.au</p>
</section>

<section class="side back">
  <div class="band title"><span>Brightwater</span><span>Circle</span></div>
  <div class="panel story"><p>Share the story of your<br>lantern cards on<br>social media with<br>the hashtag</p></div>
  <div class="band tag">#morninglanterndrive</div>
  <div class="panel send"><p>or send us a photo and<br>your story to</p></div>
  <div class="band mail">lantern@brightwatercircle.com.au</div>

  <p class="card-heading">Lantern<br>Card</p>

  <svg class="card-space" width="348" height="276" viewBox="0 0 348 276" aria-label="Space to attach a lantern card">
    <path d="M0 0 H263 V42 H348 V276 H0 Z" fill="#a9a9a9"/>
    <g stroke="#e9e9e9" stroke-width="1.5">
      <line x1="18" y1="70" x2="230" y2="70"/>
      <line x1="18" y1="108" x2="326" y2="108"/>
      <line x1="18" y1="146" x2="326" y2="146"/>
      <line x1="18" y1="184" x2="326" y2="184"/>
      <line x1="18" y1="222" x2="326" y2="222"/>
      <line x1="18" y1="260" x2="326" y2="260"/>
    </g>
  </svg>
</section>

</body>
</html>
```